Thornwell Building Company - advertisement poster

I am looking to print some canvas signs to advertise my general contracting company, Thornwell Building Company. The sign will measure 6' long x 3' high so the size should match that ratio. I already have a logo icon, which is the Letter 'A' and some trees that I would like to incorporate, see attached. I would also like the to have the following information listed:
1) phone number: 472-318-6095
2) email: thornwellbuildingcompany@mailvistra.net
3) website: thornwellbuildingcompany.com
4) Lic#5386204
5) I want to use this text: "BUILD WITH THE T-CREW!"

The ad should be relatively simple and clean. Black and Green are my company colors. I am open to creative ideas!

Target Market(s)

People looking to renovate their homes

Industry/Entity Type

Construction

Colors
59FF00
82FF00
B8FF75
E3FFCB
F4FFEA

Requirements
Must have
• Must have my company logo
Should not have
• No photos or complex graphics

```html
<!DOCTYPE html>
<html lang="en">
<head>
<meta charset="utf-8">
<title>Thornwell Building Company – Canvas Sign</title>
<link rel="stylesheet" href="https://fonts.googleapis.com/css2?family=Montserrat:ital,wght@0,400;0,600;0,700;0,800;1,900&display=swap">
<style>
  :root {
    --stage: #8e8e8e;
    --paper: #ffffff;
    --ink: #000000;
    --navy: #00008f;
    --lime: #66f500;
    --brand-green: #59ff00;
    --faint: #2a2c28;
    --white: #ffffff;
  }
  * { margin: 0; padding: 0; box-sizing: border-box; }
  html, body { width: 1200px; height: 1200px; overflow: hidden; }
  body { background: var(--stage); font-family: "Montserrat", sans-serif; position: relative; }

  .sign { position: absolute; left: 31px; top: 315px; width: 1138px; height: 569px; background: var(--paper); }

  .slogan { position: absolute; left: 53px; top: 100px; }
  .slogan-main {
    font-weight: 900; font-style: italic; font-size: 106px; line-height: 1;
    color: var(--navy); letter-spacing: -3px;
  }
  .slogan-sub {
    margin-top: 4px; font-weight: 800; font-size: 42px; line-height: 1;
    color: var(--navy); display: flex; align-items: center; gap: 9px;
  }
  .slogan-highlight { background: var(--lime); color: var(--white); padding: 3px 8px 3px 6px; }

  .divider { position: absolute; left: 452px; top: 95px; width: 2px; height: 177px; background: var(--ink); }

  .contact { position: absolute; left: 499px; top: 102px; list-style: none; }
  .contact li { font-size: 23px; line-height: 42px; color: var(--ink); font-weight: 400; white-space: nowrap; }
  .contact .label { font-weight: 700; }

  .brand-band { position: absolute; left: 0; top: 359px; width: 1138px; height: 210px; background: var(--ink); }

  .brand-lockup {
    position: absolute; left: 50%; top: 50%; transform: translate(-50%, -50%);
    display: flex; flex-direction: column; align-items: center;
  }
  .brand-est { display: flex; justify-content: center; gap: 110px; margin-bottom: 16px; }
  .brand-est span {
    font-size: 11px; letter-spacing: 4px; color: var(--white); font-weight: 400; line-height: 1;
    border-top: 1px solid var(--brand-green); border-bottom: 1px solid var(--brand-green); padding: 5px 6px;
  }
  .brand-name { display: flex; align-items: center; gap: 14px; }
  .brand-mark { flex: none; width: 22px; height: 22px; background: var(--brand-green); }
  .brand-text {
    font-weight: 700; font-size: 30px; line-height: 1.2; letter-spacing: 1px;
    color: var(--white); text-align: left;
  }
  .brand-text span { display: block; white-space: nowrap; }

  .brand-faint {
    position: absolute; top: 50%; transform: translateY(-50%);
    width: 170px; display: flex; align-items: center; gap: 8px;
  }
  .brand-faint.left { left: 42px; }
  .brand-faint.right { right: 42px; }
  .brand-faint .brand-mark { width: 12px; height: 12px; background: var(--faint); }
  .brand-faint .brand-text { font-size: 14px; line-height: 1.25; color: var(--faint); letter-spacing: 0.5px; }
</style>
</head>
<body>
  <main class="sign">
    <div class="slogan">
      <div class="slogan-main">BUILD</div>
      <div class="slogan-sub">With the <span class="slogan-highlight">T-Crew</span></div>
    </div>

    <div class="divider"></div>

    <ul class="contact">
      <li><span class="label">Phone No.:</span> 472-318-6095</li>
      <li><span class="label">email</span>: thornwellbuildingcompany@mailvistra.net</li>
      <li><span class="label">website:</span> thornwellbuildingcompany.com</li>
      <li><span class="label">Lic#</span> 5386204</li>
    </ul>

    <footer class="brand-band">
      <div class="brand-faint left">
        <span class="brand-mark"></span>
        <span class="brand-text"><span>Thornwell</span><span>Building Company</span></span>
      </div>

      <div class="brand-lockup">
        <div class="brand-est"><span>ESTD</span><span>2020</span></div>
        <div class="brand-name">
          <span class="brand-mark"></span>
          <span class="brand-text"><span>Thornwell</span><span>Building Company</span></span>
        </div>
      </div>

      <div class="brand-faint right">
        <span class="brand-mark"></span>
        <span class="brand-text"><span>Thornwell</span><span>Building Company</span></span>
      </div>
    </footer>
  </main>
</body>
</html>
```